Updated brochure for academic IT services unit

We are an IT service and support group serving many academic and administrative departments in the School of Verse and Inquiry (https://verseandinquiry.brenholt.edu) at the Marrowfield State Institute, Davis (https://www.brenholt.edu/). Our clients are the faculty, staff, researchers, and graduate students in the departments we support. We have an existing brochure (attached) that is sent to all of our clients at the start of each school year. The primary objective of the brochure is to provide contact information for clients to engage our services, and a secondary objective is to provide some brief updates on new or changed services that are offered. We are currently renaming as a result of a recent expansion in our scope to cover 25% more departments/clients, and we have not updated the brochure design in several years. So, we are looking for an updated design that will appeal to our new clients as well as our existing clients. Some requirements for the design include:* Since we are a MS Tarnow unit, we need to follow the university branding and visual identity guidelines, available here: https://brandkit.brenholt.edu* Our team has expanded to 21 career staff and ~25 student staff, so we need to find a way to fit that information onto the brochure.* While the current brochure is tri-fold 8.5 x 11, we are open to other formats.* Some messages we want to communicate are that 1. we are readily available and happy to help, 2. we have a lot of technical expertise, 3. contacting our service desk via phone is the fastest way to get support.

Target Market(s)

Internal clients: faculty, staff, researchers and graduate students in humanities, arts, cultural studies, and social sciences departments.

Font styles to use
Other font styles liked:
• Berkeley MS Tarnow and Proxima Nova, https://brandkit.brenholt.edu/visual-identity/fonts.html

Requirements
Must have
• * Since we are a MS Tarnow unit, we need to follow the university branding and visual identity guidelines, available here: https://brandkit.brenholt.edu
• * Our team has expanded to 21 career staff and ~25 student staff, so we need to find a way to fit that information onto the brochure.
Nice to have
• * While the current brochure is tri-fold 8.5 x 11, we are open to other formats.
• * Some messages we want to communicate are that 1. we are readily available and happy to help, 2. we have a lot of technical expertise, 3. contacting our service desk via phone is the fastest way to get support.

```html
<!DOCTYPE html>
<html lang="en">
<head>
<meta charset="utf-8">
<title>Verse &amp; Inquiry IT Service Center — Tri-fold Brochure</title>
<link rel="stylesheet" href="https://fonts.googleapis.com/css2?family=Montserrat:wght@400;600;700;800;900&family=Crimson+Text:ital,wght@0,400;0,600;1,400;1,600&family=Open+Sans:wght@400;600;700&display=swap">
<style>
:root{
  --navy:#12305f;
  --navy-deep:#0d2550;
  --gold:#f5b41c;
  --white:#ffffff;
  --paper:#ffffff;
  --band:#ececec;
  --ink:#1d2433;
  --muted:#6b7280;
  --link:#2f6fb5;
  --stage:#e7eaf0;
  --photo-a:#b9b2a8;
  --photo-b:#8a8f99;
}
*{box-sizing:border-box;margin:0;padding:0}
html,body{width:1200px;height:1200px;overflow:hidden}
body{background:var(--stage);font-family:"Open Sans",Arial,sans-serif;color:var(--ink);position:relative}

.spread{position:absolute;left:30px;width:1140px;height:572px;display:flex;box-shadow:0 2px 10px rgba(13,37,80,.18)}
.spread--outside{top:20px}
.spread--inside{top:608px}
.panel{position:relative;width:380px;height:572px;background:var(--paper);overflow:hidden}
.panel + .panel{border-left:1px solid #d9dde4}
.wave{position:absolute;left:0;top:0;width:380px}

.section-title{font-family:"Montserrat",sans-serif;font-weight:700;font-size:9.5px;color:var(--navy);padding-bottom:4px;border-bottom:1.5px dotted #8a93a3;margin-bottom:6px}
.photo{background:linear-gradient(160deg,var(--photo-a),var(--photo-b));flex:none}
.name{font-family:"Crimson Text",serif;font-style:italic;font-weight:600;color:var(--navy)}

/* ---------- Our People ---------- */
.people__title{position:absolute;left:34px;top:26px;font-family:"Montserrat",sans-serif;font-weight:900;font-size:33px;line-height:1.05;color:var(--white)}
.director__portrait{position:absolute;left:242px;top:24px;width:120px;height:120px;border-radius:50%;border:6px solid var(--white);background:linear-gradient(160deg,#b7aea3,#6f7480)}
.director__caption{position:absolute;right:18px;top:154px;text-align:right}
.director__name{font-family:"Crimson Text",serif;font-size:17px;font-weight:600;color:var(--navy)}
.director__role{font-size:10px;color:var(--muted);margin-right:18px}
.team{position:absolute;left:16px;right:14px}
.team--desk{top:196px}
.team--split{top:340px;display:flex;gap:12px}
.team--split > div{flex:1}
.team--research{top:484px;width:190px}
.staff-grid{display:grid;grid-template-columns:1fr 1fr;row-gap:5px;column-gap:8px}
.staff{display:flex;align-items:center;gap:6px;height:34px}
.staff .photo{width:30px;height:34px}
.staff .name{font-size:12px;line-height:1.1}
.staff__role{font-size:6.2px;color:var(--muted);line-height:1.2}
.staff-list{display:flex;flex-direction:column;gap:5px}

/* ---------- Contact ---------- */
.headline{position:absolute;left:0;right:0;top:22px;text-align:center;color:var(--white)}
.headline__big{font-family:"Montserrat",sans-serif;font-weight:900;font-size:25px;line-height:1.12}
.headline__small{font-family:"Crimson Text",serif;font-size:17px;margin-top:2px}
.contact__title{position:absolute;left:0;right:0;top:188px;text-align:center;font-family:"Montserrat",sans-serif;font-weight:700;font-size:22px;color:var(--navy)}
.contact__lead{position:absolute;left:30px;right:30px;top:222px;text-align:center;font-family:"Crimson Text",serif;font-style:italic;font-size:10.5px;line-height:1.35}
.contact__phone{position:absolute;left:0;right:0;top:252px;display:flex;justify-content:center;align-items:center;gap:10px;font-family:"Montserrat",sans-serif;font-weight:700;font-size:25px;color:var(--gold)}
.contact__band{position:absolute;left:0;right:0;top:292px;height:110px;background:var(--band);display:flex;padding:12px 12px 0}
.contact__col{flex:1;text-align:center;font-family:"Crimson Text",serif;font-size:10px;line-height:1.7}
.contact__col h3{font-family:"Crimson Text",serif;font-style:italic;font-weight:400;font-size:13px;margin-bottom:4px}
.contact__col svg{display:block;margin:2px auto 0}
.hours{position:absolute;left:12px;right:12px;top:408px;font-family:"Crimson Text",serif;font-style:italic;font-size:10px;line-height:1.35}
.hours h3{font-family:"Montserrat",sans-serif;font-style:normal;font-weight:700;font-size:11px;color:var(--navy);margin:6px 0 2px}
.contact__footer{position:absolute;left:0;bottom:0;width:380px}
.contact__footer-text{position:absolute;left:0;right:0;bottom:10px;text-align:center;font-family:"Montserrat",sans-serif;font-weight:600;font-size:17px;color:var(--white)}

/* ---------- Cover ---------- */
.cover__photo{position:absolute;left:0;right:0;top:200px;bottom:0;background:linear-gradient(180deg,#5d93d6 0%,#9cc4ea 30%,#c9875e 55%,#a7a08c 75%,#6d7560 100%)}
.cover__title{position:absolute;left:30px;right:16px;top:42px;font-family:"Montserrat",sans-serif;font-weight:900;font-size:26px;line-height:1.18;color:var(--white)}
.cover__tagline{position:absolute;left:30px;top:116px;font-family:"Crimson Text",serif;font-size:19px;color:var(--white);letter-spacing:.3px}
.call-badge{position:absolute;left:228px;top:168px;width:144px;height:144px;border-radius:50%;background:var(--gold);border:6px solid var(--white);display:flex;flex-direction:column;align-items:center;justify-content:center;color:var(--navy-deep)}
.call-badge__label{font-family:"Montserrat",sans-serif;font-weight:700;font-size:23px}
.call-badge__phone{font-family:"Montserrat",sans-serif;font-weight:700;font-size:13px;margin-top:2px}

/* ---------- Do You Need ---------- */
.need__title{position:absolute;left:26px;top:30px;color:var(--white);font-family:"Montserrat",sans-serif}
.need__title span{display:block;font-size:18px;font-weight:400}
.need__title strong{display:block;font-size:22px;font-weight:800;letter-spacing:.5px}
.need__body{position:absolute;left:16px;right:16px;top:150px}
.q{font-family:"Montserrat",sans-serif;font-weight:700;font-size:10px;color:var(--navy);line-height:1.3;margin:10px 0 6px}
.copy{font-size:6.6px;line-height:1.5;color:var(--ink)}
.copy + .copy{margin-top:6px}
.copy a{color:var(--link);text-decoration:none}
.with-art{display:flex;gap:10px;align-items:center}
.with-art .copy-wrap{flex:1}
.art{flex:none}
.art--laptop{width:92px;height:78px;background:linear-gradient(150deg,#3b4150,#0f1116);border-radius:4px}
.art--apps{width:84px;height:84px;background:linear-gradient(140deg,#4aa3df,#e0457b 50%,#f5b41c);border-radius:10px;opacity:.85}

/* ---------- Services ---------- */
.services{position:absolute;left:12px;right:14px;top:28px}
.services .q{margin-top:0}
.service-block{margin-bottom:14px}
.art--printer{width:112px;height:84px;background:linear-gradient(180deg,#d8dadd,#3a3d42);border-radius:4px}
.art--chart{width:86px;height:86px;border-radius:50%;border:5px solid var(--navy);background:linear-gradient(135deg,#ffffff,#e6eef6)}
.site-builder{font-family:"Montserrat",sans-serif;font-weight:700;font-size:15px;color:var(--gold);width:92px;text-align:center}
.concerns{position:absolute;left:0;right:0;bottom:0;height:168px;background:var(--gold);color:var(--white);text-align:center;padding-top:14px;font-family:"Montserrat",sans-serif}
.concerns__eyebrow{font-size:14px;font-weight:400;letter-spacing:.4px}
.concerns__head{font-size:18px;font-weight:900;margin-top:-2px}
.concerns__role{font-size:10.5px;margin-top:8px}
.concerns__name{font-size:13px;font-weight:700}
.concerns__email{font-size:12px;font-family:"Open Sans",sans-serif;margin-top:8px}
.concerns__phone{font-size:20px;font-weight:800;margin-top:6px}

/* ---------- Students ---------- */
.students{position:absolute;left:16px;right:16px;top:26px}
.students .section-title{font-size:10.5px;margin-bottom:10px}
.student-grid{display:grid;grid-template-columns:repeat(3,1fr);row-gap:6px;column-gap:14px}
.student{text-align:center}
.student .photo{width:100%;height:66px}
.student .name{font-size:10px;display:block;margin-top:1px;color:var(--ink)}
</style>
</head>
<body>

<section class="spread spread--outside">

  <article class="panel panel--people">
    <svg class="wave" height="190" viewBox="0 0 380 190" preserveAspectRatio="none" aria-hidden="true">
      <path d="M0 0H380V150C290 120 170 150 0 180Z" fill="var(--gold)"/>
      <path d="M0 0H380V132C290 104 170 134 0 164Z" fill="var(--navy)"/>
    </svg>
    <h1 class="people__title">Our<br>People</h1>
    <div class="director__portrait" role="img" aria-label="Portrait photo of the IT director"></div>
    <div class="director__caption">
      <div class="director__name">Corwin Hallett</div>
      <div class="director__role">IT Director</div>
    </div>

    <div class="team team--desk">
      <h2 class="section-title">Service Desk &amp; Desktop Support</h2>
      <div class="staff-grid">
        <div class="staff"><div class="photo" role="img" aria-label="Staff headshot"></div><div><div class="name">Marisol Pende</div><div class="staff__role">Service Desk and Desktop Manager</div></div></div>
        <div class="staff"><div class="photo" role="img" aria-label="Staff headshot"></div><div><div class="name">Tobin Ashgrove</div><div class="staff__role">Senior Desktop Support Analyst</div></div></div>
        <div class="staff"><div class="photo" role="img" aria-label="Staff headshot"></div><div><div class="name">Ilario Benz</div><div class="staff__role">Service Desk Analyst</div></div></div>
        <div class="staff"><div class="photo" role="img" aria-label="Staff headshot"></div><div><div class="name">Dorian Keane</div><div class="staff__role">Desktop Support Analyst</div></div></div>
        <div class="staff"><div class="photo" role="img" aria-label="Staff headshot"></div><div><div class="name">Renley Tsao</div><div class="staff__role">Desktop Support Analyst</div></div></div>
      </div>
    </div>

    <div class="team team--split">
      <div>
        <h2 class="section-title">System Administration</h2>
        <div class="staff-list">
          <div class="staff"><div class="photo" role="img" aria-label="Staff headshot"></div><div><div class="name">Aldous Finch</div><div class="staff__role">Lead Systems Administrator</div></div></div>
          <div class="staff"><div class="photo" role="img" aria-label="Staff headshot"></div><div><div class="name">Bram Olsted</div><div class="staff__role">Systems Administrator</div></div></div>
          <div class="staff"><div class="photo" role="img" aria-label="Staff headshot"></div><div><div class="name">Lionel Garrow</div><div class="staff__role">Systems Administrator</div></div></div>
        </div>
      </div>
      <div>
        <h2 class="section-title">Application Development</h2>
        <div class="staff-list">
          <div class="staff"><div class="photo" role="img" aria-label="Staff headshot"></div><div><div class="name">Everett Lindqvist</div><div class="staff__role">Lead Application Developer</div></div></div>
          <div class="staff"><div class="photo" role="img" aria-label="Staff headshot"></div><div><div class="name">Percival Dunmore</div><div class="staff__role">Application Developer</div></div></div>
          <div class="staff"><div class="photo" role="img" aria-label="Staff headshot"></div><div><div class="name">Odette Varga</div><div class="staff__role">Webmaster</div></div></div>
        </div>
      </div>
    </div>

    <div class="team team--research">
      <h2 class="section-title">Computational Research Service</h2>
      <div class="staff"><div class="photo" role="img" aria-label="Staff headshot"></div><div><div class="name">Felix Marden</div><div class="staff__role">Statistical Programming Consultant</div></div></div>
    </div>

    <svg class="wave" style="top:auto;bottom:0" height="60" viewBox="0 0 380 60" preserveAspectRatio="none" aria-hidden="true">
      <path d="M230 60C290 40 340 22 380 10V60Z" fill="var(--gold)"/>
      <path d="M280 60C320 46 355 34 380 28V60Z" fill="var(--navy)"/>
    </svg>
  </article>

  <article class="panel panel--contact">
    <svg class="wave" height="180" viewBox="0 0 380 180" preserveAspectRatio="none" aria-hidden="true">
      <path d="M0 0H380V170C280 130 130 180 0 150Z" fill="var(--gold)"/>
      <path d="M0 0H380V150C280 116 130 160 0 128Z" fill="var(--navy)"/>
    </svg>
    <div class="headline">
      <div class="headline__big">21 career staff &amp;<br>+25 student staff</div>
      <div class="headline__small">are waiting here to help you.</div>
    </div>

    <h2 class="contact__title">Contact</h2>
    <p class="contact__lead">For fastest support give us a call. Within 30 minutes (service hours) our representative will help you.</p>
    <div class="contact__phone">
      <svg width="22" height="22" viewBox="0 0 24 24" aria-hidden="true"><path fill="var(--navy)" d="M6.6 10.8a15.1 15.1 0 0 0 6.6 6.6l2.2-2.2a1 1 0 0 1 1-.25 11.4 11.4 0 0 0 3.6.57 1 1 0 0 1 1 1V20a1 1 0 0 1-1 1A17 17 0 0 1 3 4a1 1 0 0 1 1-1h3.5a1 1 0 0 1 1 1c0 1.25.2 2.45.57 3.570a1 1 0 0 1-.25 1z"/></svg>
      530-555-0142
    </div>

    <div class="contact__band">
      <div class="contact__col">
        <h3>Website &amp; Email</h3>
        <svg width="11" height="11" viewBox="0 0 12 12" aria-hidden="true"><circle cx="6" cy="6" r="5" fill="none" stroke="var(--navy)" stroke-width="1.4"/><path d="M1 6h10M6 1c2.5 2.8 2.5 7.2 0 10M6 1c-2.5 2.8-2.5 7.2 0 10" fill="none" stroke="var(--navy)" stroke-width="1"/></svg>
        http://it.vi.brenholt.edu
        <svg width="12" height="9" viewBox="0 0 12 9" aria-hidden="true"><rect x=".5" y=".5" width="11" height="8" fill="var(--navy)"/><path d="M.5 .5 6 5l5.5-4.5" fill="none" stroke="var(--band)" stroke-width="1"/></svg>
        ithelp@it.vi.brenholt.edu
      </div>
      <div class="contact__col">
        <h3>Drop In Locations</h3>
        2235 V&amp;I Hall<br>483 Ashby Hall<br>8 Pellam Hall<br>267 Corrin Hall, Room 137
      </div>
    </div>

    <div class="hours">
      <h3>Computational Research Service</h3>
      Monday–Friday, 9AM–5PM<br>530-555-0187<br>0105 V&amp;I Hall
      <h3>Service Hours</h3>
      Monday–Friday, 7:30AM–6PM
    </div>

    <svg class="contact__footer" height="56" viewBox="0 0 380 56" preserveAspectRatio="none" aria-hidden="true">
      <path d="M0 24C120 10 260 4 380 0V56H0Z" fill="var(--gold)"/>
      <path d="M0 32C120 18 260 12 380 8V56H0Z" fill="var(--navy)"/>
    </svg>
    <div class="contact__footer-text">Call us anytime</div>
  </article>

  <article class="panel panel--cover">
    <div class="cover__photo" role="img" aria-label="Photo of a student cycling past a sunlit campus building"></div>
    <svg class="wave" height="260" viewBox="0 0 380 260" preserveAspectRatio="none" aria-hidden="true">
      <path d="M0 0H380V240C260 190 120 250 0 200Z" fill="var(--gold)"/>
      <path d="M0 0H380V222C260 172 120 232 0 182Z" fill="var(--navy)"/>
    </svg>
    <h1 class="cover__title">Verse &amp; Inquiry<br>IT Service Center</h1>
    <p class="cover__tagline">Happy To Help You Anytime</p>
    <div class="call-badge">
      <span class="call-badge__label">Call Us</span>
      <span class="call-badge__phone">530-555-0142</span>
    </div>
  </article>
</section>

<section class="spread spread--inside">

  <article class="panel panel--need">
    <svg class="wave" height="150" viewBox="0 0 380 150" preserveAspectRatio="none" aria-hidden="true">
      <path d="M0 0H300C290 70 250 128 140 138C80 143 30 140 0 136Z" fill="var(--gold)"/>
      <path d="M0 0H284C272 60 236 112 136 120C76 125 30 122 0 118Z" fill="var(--navy)"/>
    </svg>
    <div class="need__title"><span>Do You</span><strong>NEED.....</strong></div>

    <div class="need__body">
      <h3 class="q">Get support or ask a general question? Borrow equipment or IT supplies?</h3>
      <p class="copy">Our service desk is open from 7:30AM to 6PM. Give us a call, send us an email, visit our website or just drop by! We lend laptops, printers, cables, video adapters, conferencing gear and other items kept in stock and available for loan. See contact info to the left.</p>

      <h3 class="q">Get support or ask a general question? Borrow equipment or IT supplies?</h3>
      <div class="with-art">
        <div class="copy-wrap">
          <p class="copy">The Verse &amp; Inquiry Computer Replacement Program provides one laptop or desktop computer every five years for Senate faculty, continuing lecturers, and career staff. Just contact the service desk to start the process or visit <a>http://it.vi.brenholt.edu/purchasing/computer-replacement</a>.</p>
          <p class="copy">To purchase a computer or any other IT equipment, just contact the service desk. You can find our recommended models on the Verse &amp; Inquiry IT website at http://it.vi.brenholt.edu/purchasing</p>
        </div>
        <div class="art art--laptop" role="img" aria-label="Illustration of an open laptop"></div>
      </div>

      <h3 class="q" style="margin-top:18px">Get software or web services?</h3>
      <div class="with-art">
        <div class="copy-wrap">
          <p class="copy">Verse &amp; Inquiry and MS Tarnow provide Quillworks Office, Folio Reader (for faculty and staff), and many other packages at no cost. Packages including Numeris, StatLens, and many others are available at reduced cost. More info at <a>http://it.vi.brenholt.edu/purchasing/software</a>.</p>
          <p class="copy">Many web-based services are available at no or low cost, including unlimited online surveys, Cratebox storage and syncing, Surveyor, SafeKeep online backup, and CodeHarbor. Find more in the campus IT catalog at <a>http://itcatalog.brenholt.edu/</a></p>
        </div>
        <div class="art art--apps" role="img" aria-label="Illustration of a cluster of colourful app icons"></div>
      </div>
    </div>
  </article>

  <article class="panel panel--services">
    <div class="services">
      <div class="service-block">
        <h3 class="q">Print a poster?</h3>
        <div class="with-art">
          <div class="copy-wrap">
            <p class="copy">Verse &amp; Inquiry IT prints posters on our 42-inch printers for $33. Request a poster at <a>http://it.vi.brenholt.edu/catalog/printing/poster-printing-request</a></p>
          </div>
          <div class="art art--printer" role="img" aria-label="Photo of a large-format poster printer"></div>
        </div>
      </div>

      <div class="service-block">
        <h3 class="q">Consult with a computational research and statistics expert? Access stats software?</h3>
        <div class="with-art">
          <div class="copy-wrap">
            <p class="copy">Verse &amp; Inquiry IT welcomes Felix Marden and the Computational Research Service (formerly the Verse Data Service) to our unit! Felix provides consulting and research computing services to all faculty, graduate students and researchers in our departments. Find more information at <a>http://www.rds.brenholt.edu</a></p>
          </div>
          <div class="art art--chart" role="img" aria-label="Illustration of colourful statistics charts in a circle"></div>
        </div>
      </div>

      <div class="service-block">
        <h3 class="q">Set up a website for lab, project, conference, or yourself?</h3>
        <div class="with-art">
          <div class="copy-wrap">
            <p class="copy">Verse &amp; Inquiry IT offers Pagewright, an easy to use platform for quickly creating attractive websites for faculty members, labs, projects or conferences. You can request a new Pagewright site at <a>http://it.vi.brenholt.edu/services/websites/pagewright-request</a>.</p>
            <p class="copy">Verse &amp; Inquiry and MS Tarnow provide a number of other website options, which you can explore at <a>http://it.vi.brenholt.edu/services/websites</a></p>
          </div>
          <div class="site-builder">Pagewright</div>
        </div>
      </div>
    </div>

    <div class="concerns">
      <div class="concerns__eyebrow">QUESTIONS OR CONCERNS</div>
      <div class="concerns__head">ABOUT OUR SERVICE?</div>
      <div class="concerns__role">Verse &amp; Inquiry IT Director</div>
      <div class="concerns__name">Corwin Hallett</div>
      <div class="concerns__email">corwin@brenholt.edu</div>
      <div class="concerns__phone">530-555-0199</div>
    </div>
  </article>

  <article class="panel panel--students">
    <div class="students">
      <h2 class="section-title">Student Service Analysts</h2>
      <div class="student-grid">
        <div class="student"><div class="photo" role="img" aria-label="Student headshot"></div><span class="name">Arlo M.</span></div>
        <div class="student"><div class="photo" role="img" aria-label="Student headshot"></div><span class="name">Kenji S.</span></div>
        <div class="student"><div class="photo" role="img" aria-label="Student headshot"></div><span class="name">Rowan T.</span></div>
        <div class="student"><div class="photo" role="img" aria-label="Student headshot"></div><span class="name">Desmond A.</span></div>
        <div class="student"><div class="photo" role="img" aria-label="Student headshot"></div><span class="name">Quincy L.</span></div>
        <div class="student"><div class="photo" role="img" aria-label="Student headshot"></div><span class="name">Milo R.</span></div>
        <div class="student"><div class="photo" role="img" aria-label="Student headshot"></div><span class="name">Hyun P.</span></div>
        <div class="student"><div class="photo" role="img" aria-label="Student headshot"></div><span class="name">Ezra V.</span></div>
        <div class="student"><div class="photo" role="img" aria-label="Student headshot"></div><span class="name">Theo N.</span></div>
        <div class="student"><div class="photo" role="img" aria-label="Student headshot"></div><span class="name">Linus C.</span></div>
        <div class="student"><div class="photo" role="img" aria-label="Student headshot"></div><span class="name">Oscar W.</span></div>
        <div class="student"><div class="photo" role="img" aria-label="Student headshot"></div><span class="name">Priya D.</span></div>
        <div class="student"><div class="photo" role="img" aria-label="Student headshot"></div><span class="name">Emil Jay K.</span></div>
        <div class="student"><div class="photo" role="img" aria-label="Student headshot"></div><span class="name">Silas F.</span></div>
        <div class="student"><div class="photo" role="img" aria-label="Student headshot"></div><span class="name">Nora E.</span></div>
        <div class="student"><div class="photo" role="img" aria-label="Student headshot"></div><span class="name">Jasper H.</span></div>
        <div class="student"><div class="photo" role="img" aria-label="Student headshot"></div><span class="name">Dante O.</span></div>
        <div class="student"><div class="photo" role="img" aria-label="Student headshot"></div><span class="name">Callum Y.</span></div>
      </div>
    </div>
  </article>
</section>

</body>
</html>
```